High Tech Real Estate Startup needs a business card

We are developing an innovative real estate marketing product based around advanced search and virtual reality.

We talk to people, we need business cards.

Target Market(s)

The target market is technology professionals and realtors.

Contact Information for Business Card

The information to be included will include

Name
Title
Phone Number
E-mail Address
www.quelzo.com

It should use simple iconography for each one of those fields.

Font styles to use
Other font styles liked:
• Co, Jubilat, Avenir

Colors

Designer to choose colors to be used in the design.

Requirements
Must have
• Clean aesthetic,
• Good use of negative space.
• It should use our company logo, shown in the attached file. It is able to use the negative of that logo (coloured font and white background) and I have attached other acceptable accent colours in a swatch file.
Should not have
• Should not be too busy
• No extraneous text (slogans, tag lines etc)

```html
<!DOCTYPE html>
<html lang="en">
<head>
<meta charset="utf-8">
<title>Quelzo Business Card</title>
<link href="https://fonts.googleapis.com/css2?family=Lato:wght@400;700&display=swap" rel="stylesheet">
<style>
  :root {
    --stage: #3d3d3d;
    --teal: #00b9be;
    --teal-soft: #12c1c6;
    --paper: #ffffff;
    --ink: #3a3a3a;
    --rule: #8a8fb0;
  }
  * { margin: 0; padding: 0; box-sizing: border-box; }
  html, body {
    width: 1200px; height: 900px; overflow: hidden;
    background: var(--stage);
    font-family: "Lato", sans-serif;
  }
  .canvas { position: relative; width: 1200px; height: 900px; }
  .card {
    position: absolute; top: 170px; width: 347px; height: 561px;
    box-shadow: 3px 3px 5px rgba(0,0,0,0.55);
  }
  .card--front { left: 259px; background: var(--paper); }
  .card--back { left: 631px; background: var(--teal); overflow: hidden; }

  .logo-block {
    position: absolute; left: 69px; top: 56px; width: 211px; height: 210px;
    background: var(--teal);
    display: flex; align-items: center; justify-content: center;
  }
  .logo-name {
    color: var(--paper); font-weight: 400; font-size: 38px; letter-spacing: 2px;
    margin-top: -18px;
  }

  .contact { position: absolute; left: 0; right: 0; top: 370px; text-align: center; }
  .contact-name {
    color: var(--teal); font-weight: 700; font-size: 24px; letter-spacing: 0.3px; line-height: 1;
  }
  .contact-title {
    color: var(--ink); font-size: 14px; margin-top: 6px; letter-spacing: 0.2px;
  }
  .contact-rule {
    width: 157px; height: 1px; background: var(--rule); margin: 14px auto 12px;
  }
  .contact-line { color: var(--ink); font-size: 16px; line-height: 25px; }
  .contact-label { color: var(--teal); font-weight: 700; }
  .contact-web { color: var(--teal); font-weight: 700; font-size: 16px; line-height: 26px; }

  .back-texture {
    position: absolute; inset: 0;
    background: linear-gradient(160deg, var(--teal-soft) 0%, var(--teal) 70%);
  }
  .back-name {
    position: absolute; left: 0; right: 0; top: 410px; text-align: center;
    color: var(--paper); font-weight: 400; font-size: 70px; letter-spacing: 3px; line-height: 1;
  }
</style>
</head>
<body>
<main class="canvas">
  <section class="card card--front">
    <div class="logo-block"><span class="logo-name">QUELZO</span></div>
    <div class="contact">
      <p class="contact-name">MARISOL BRENNAN</p>
      <p class="contact-title">MANAGING DIRECTOR</p>
      <div class="contact-rule"></div>
      <p class="contact-line"><span class="contact-label">P:</span> 555-210-4837</p>
      <p class="contact-line"><span class="contact-label">E:</span> INFO@QUELZO.COM</p>
      <p class="contact-web">WWW.QUELZO.COM</p>
    </div>
  </section>
  <section class="card card--back">
    <div class="back-texture" role="img" aria-label="Faint diagonal repeating brand-name texture"></div>
    <p class="back-name">QUELZO</p>
  </section>
</main>
</body>
</html>
```